Quiet Harbor Path - Web design

I require a complete design for a responsive 3 page business website.

High end design type, similar to (in order of preference):
]https://brennaolstead.co/
https://riverstone-guidance-wellbeing.com.au/
https://calmridgementoring.com.au/
https://buildyourglow.com/
https://theclearpathguide.com/
https://www.dervlakempson.com/
https://theloom.com/

Please use the attached old company logo, which is to be used a reference for the new branding and design.

Please use the colour palette below
#3D3D3D
#FBF8F3
#CAAD53
#7EB492
#EDCFBF

Target Market(s)

Male & female 30-50s, small business owners and executive corporates, first world english speaking nations.

Industry/Entity Type

Life Coaching

Logo Text

Quiet Harbor Path. Tagline: Holistic Transformational Coaching

Number of Pages Required

3 page

Font styles to use
Sans Serif

Requirements
Must have
• Testimonials section, google reivews section, book online button.

```html
<!DOCTYPE html>
<html lang="en">
<head>
<meta charset="UTF-8">
<title>Brightmere — Transformational Life Coaching</title>
<link rel="stylesheet" href="https://fonts.googleapis.com/css2?family=Lato:wght@300;400;700&family=Montserrat:wght@400&display=swap">
<style>
  :root {
    --ink: #3d3d3d;
    --cream: #ffffff;
    --gold: #caad53;
    --brand: #8d7c43;
    --blush: #edcfbf;
    --blush-soft: #f4e0d6;
    --avatar: #3d3d3d;
  }
  * { box-sizing: border-box; margin: 0; padding: 0; }
  html, body { width: 1200px; height: 1062px; overflow: hidden; background: var(--cream); }
  body { position: relative; font-family: "Lato", sans-serif; color: var(--ink); }

  .site-header { position: absolute; left: 94px; top: 40px; width: 1007px; height: 40px; }
  .brand { position: absolute; left: 0; top: 4px; display: flex; align-items: center; gap: 8px; color: var(--brand); }
  .brand-mark { width: 20px; height: 20px; border-radius: 50%; background: var(--gold); }
  .brand-name { font-family: "Lato", sans-serif; font-weight: 400; font-size: 22px; letter-spacing: 1px; line-height: 1; text-transform: uppercase; }
  .brand-tagline { display: block; font-size: 6px; letter-spacing: 1.4px; margin-top: 4px; text-transform: uppercase; }
  .main-nav { position: absolute; right: 0; top: 15px; display: flex; gap: 0; }
  .main-nav a { font-family: "Montserrat", sans-serif; font-size: 11.5px; color: var(--ink); text-decoration: none; letter-spacing: 0.2px; }
  .main-nav a + a { margin-left: 88px; }

  .hero-copy { position: absolute; left: 94px; top: 234px; width: 330px; }
  .hero-title { font-weight: 700; font-size: 30px; line-height: 35px; color: var(--ink); }
  .hero-text { margin-top: 18px; font-size: 11.5px; line-height: 20px; color: var(--ink); }
  .btn-contact { display: inline-block; margin-top: 16px; width: 124px; height: 31px; border-radius: 16px; background: var(--gold); color: #fff; font-size: 11.5px; line-height: 31px; text-align: center; text-decoration: none; }

  .hero-photo { position: absolute; left: 487px; top: 132px; width: 614px; height: 404px;
    background: linear-gradient(180deg, #d9c79a 0%, #caa064 18%, #3a3a2c 22%, #b99676 30%, #a49a95 55%, #8f8585 75%, #4a3b30 88%, #2f2a24 100%); }

  .testimonials-title { position: absolute; top: 590px; left: 0; width: 1200px; text-align: center; font-weight: 700; font-size: 31px; color: var(--ink); }

  .cards { position: absolute; top: 666px; left: 100px; display: flex; gap: 50px; }
  .card { width: 300px; height: 262px; background: #fff; box-shadow: 0 6px 18px rgba(0,0,0,0.08); position: relative; }
  .quote-icon { position: absolute; left: 22px; top: 26px; width: 50px; height: 40px; }
  .quote-text { position: absolute; left: 20px; top: 90px; width: 238px; font-weight: 300; font-size: 10.5px; line-height: 18px; text-align: justify; color: var(--ink); }
  .card-author { position: absolute; left: 0; bottom: 0; width: 100%; height: 73px; background: var(--blush); display: flex; align-items: center; padding-left: 20px; }
  .author-avatar { width: 38px; height: 38px; border-radius: 50%; background: var(--avatar); }
  .author-meta { margin-left: 20px; font-size: 11px; line-height: 14px; color: #000; }
  .author-name { font-weight: 700; }
  .author-role { color: var(--ink); }
</style>
</head>
<body>
  <header class="site-header">
    <div class="brand">
      <span class="brand-mark"></span>
      <div>
        <span class="brand-name">Brightmere</span>
        <span class="brand-tagline">Transformational Life Coaching</span>
      </div>
    </div>
    <nav class="main-nav">
      <a href="#">HOME</a>
      <a href="#">ABOUT</a>
      <a href="#">BLOG</a>
      <a href="#">CONTACT</a>
    </nav>
  </header>

  <section class="hero">
    <div class="hero-copy">
      <h1 class="hero-title">Lorem ipsum dolor sit amet elit duis</h1>
      <p class="hero-text">Nibh lobortis ipsum, mollis sem consectetur at accumsan, elit. Proin odio scelerisque duis risus tincidunt sollicitudin ac. Lectus cras quis ornare donec gravida.</p>
      <a class="btn-contact" href="#">CONTACT</a>
    </div>
    <div class="hero-photo" role="img" aria-label="Woman seated cross-legged on a wooden jetty facing a lake at sunset"></div>
  </section>

  <h2 class="testimonials-title">Testimonials</h2>

  <section class="cards">
    <article class="card">
      <svg class="quote-icon" viewBox="0 0 50 40" aria-hidden="true"><path fill="#f4e0d6" d="M0 40V22C0 9 7 2 20 0v7c-6 1-9 5-9 11h9v22zM27 40V22C27 9 34 2 47 0v7c-6 1-9 5-9 11h9v22z"/></svg>
      <p class="quote-text">Lorem ipsum dolor sit amet, consectetur adipiscing elit. Sem enim pellentesque neque, maecenas ac nunc. In phasellus consectetur leo, lorem nunc, et sit cras lorem.</p>
      <div class="card-author"><span class="author-avatar"></span><div class="author-meta"><div class="author-name">Lorem</div><div class="author-role">Business owner</div></div></div>
    </article>
    <article class="card">
      <svg class="quote-icon" viewBox="0 0 50 40" aria-hidden="true"><path fill="#f4e0d6" d="M0 40V22C0 9 7 2 20 0v7c-6 1-9 5-9 11h9v22zM27 40V22C27 9 34 2 47 0v7c-6 1-9 5-9 11h9v22z"/></svg>
      <p class="quote-text">Lorem ipsum dolor sit amet, consectetur adipiscing elit. Sem enim pellentesque neque, maecenas ac nunc. In phasellus consectetur leo, lorem nunc, et sit cras lorem.</p>
      <div class="card-author"><span class="author-avatar"></span><div class="author-meta"><div class="author-name">Lorem</div><div class="author-role">Business owner</div></div></div>
    </article>
    <article class="card">
      <svg class="quote-icon" viewBox="0 0 50 40" aria-hidden="true"><path fill="#f4e0d6" d="M0 40V22C0 9 7 2 20 0v7c-6 1-9 5-9 11h9v22zM27 40V22C27 9 34 2 47 0v7c-6 1-9 5-9 11h9v22z"/></svg>
      <p class="quote-text">Lorem ipsum dolor sit amet, consectetur adipiscing elit. Sem enim pellentesque neque, maecenas ac nunc. In phasellus consectetur leo, lorem nunc, et sit cras lorem.</p>
      <div class="card-author"><span class="author-avatar"></span><div class="author-meta"><div class="author-name">Lorem</div><div class="author-role">Business owner</div></div></div>
    </article>
  </section>
</body>
</html>
```